Oven Cleaning Business owner needs business card design

Hi there,
Would like for a business card to be designed for myself, the owner of a professional oven cleaning business on the Sunshine Coast.
Would like it to look sleek, and modern-ish. Bit creative is encouraged too.
Include following:
Name/title: Corin ter Haghe, Owner
Phone number: 1300 482 916
Email: info@hearthshinecrew.com.au
Website: www.hearthshinecrew.com.au

```html
<!DOCTYPE html>
<html lang="en">
<head>
<meta charset="utf-8">
<title>Hearthshine Crew – Business Card</title>
<link href="https://fonts.googleapis.com/css2?family=Montserrat:wght@300;400;800&display=swap" rel="stylesheet">
<style>
  :root {
    --page: #d4d4d4;
    --card: #000000;
    --cyan: #19dcdf;
    --deep-teal: #063a3a;
    --white: #ffffff;
  }
  * { box-sizing: border-box; margin: 0; padding: 0; }
  html, body {
    width: 1200px; height: 913px; overflow: hidden;
    background: var(--page);
    font-family: "Montserrat", Arial, sans-serif;
  }
  .canvas {
    position: relative; width: 1200px; height: 913px;
    display: flex; flex-direction: column; align-items: center; justify-content: center; gap: 40px;
  }
  .card {
    position: relative; width: 700px; height: 400px;
    background: var(--card);
    border: 2px solid var(--cyan);
    overflow: hidden;
  }
  /* Front: contact side */
  .card-front .decor-circle {
    position: absolute; right: -40px; top: -70px;
    width: 380px; height: 380px; border-radius: 50%;
    background: var(--deep-teal);
  }
  .brand-name {
    font-weight: 800; color: var(--cyan); text-transform: uppercase;
    letter-spacing: 0.02em; line-height: 1.05;
  }
  .card-front .brand-name {
    position: absolute; left: 48px; top: 70px; font-size: 46px;
  }
  .contact-block { position: absolute; left: 48px; top: 210px; }
  .person-name { font-weight: 800; font-size: 34px; color: var(--cyan); }
  .person-title { font-weight: 300; font-size: 20px; color: var(--white); margin-top: 2px; }
  .contact-list { list-style: none; margin-top: 16px; }
  .contact-list li {
    display: flex; align-items: center; gap: 10px;
    font-weight: 300; font-size: 17px; color: var(--white); margin-bottom: 6px;
  }
  .contact-list svg { width: 16px; height: 16px; flex: none; }
  /* Back: brand side */
  .card-back { display: flex; align-items: center; justify-content: center; gap: 26px; }
  .card-back .brand-mark {
    width: 110px; height: 110px; border-radius: 50%; background: var(--cyan);
  }
  .card-back .brand-name { font-size: 54px; }
</style>
</head>
<body>
<main class="canvas">
  <section class="card card-front" aria-label="Business card front">
    <div class="decor-circle" aria-hidden="true"></div>
    <div class="brand-name">Hearthshine<br>Crew</div>
    <div class="contact-block">
      <div class="person-name">Corin ter Haghe</div>
      <div class="person-title">Owner</div>
      <ul class="contact-list">
        <li>
          <svg viewBox="0 0 24 24" aria-hidden="true"><path fill="#19dcdf" d="M6.6 10.8a15.1 15.1 0 0 0 6.6 6.6l2.2-2.2a1 1 0 0 1 1-.25 11.4 11.4 0 0 0 3.6.57 1 1 0 0 1 1 1V20a1 1 0 0 1-1 1A17 17 0 0 1 3 4a1 1 0 0 1 1-1h3.5a1 1 0 0 1 1 1c0 1.25.2 2.45.57 3.57a1 1 0 0 1-.25 1z"/></svg>
          1300 482 916
        </li>
        <li>
          <svg viewBox="0 0 24 24" aria-hidden="true"><rect x="2" y="5" width="20" height="14" rx="1" fill="#19dcdf"/><path d="M3 6l9 7 9-7" fill="none" stroke="#000" stroke-width="1.6"/></svg>
          info@hearthshinecrew.com.au
        </li>
        <li>
          <svg viewBox="0 0 24 24" aria-hidden="true"><circle cx="12" cy="12" r="10" fill="#19dcdf"/><path d="M2 12h20M12 2c3 3 3 17 0 20M12 2c-3 3-3 17 0 20" fill="none" stroke="#000" stroke-width="1.4"/></svg>
          www.hearthshinecrew.com.au
        </li>
      </ul>
    </div>
  </section>

  <section class="card card-back" aria-label="Business card back">
    <div class="brand-mark" aria-hidden="true"></div>
    <div class="brand-name">Hearthshine<br>Crew</div>
  </section>
</main>
</body>
</html>
```